Dana Wrenfield Photography Business Card

I am looking for a simple, yet elegant business card for my photography business.

It is a short turn around project as the cards need to be printed within 48 hours. So the earlier you submit, the more likely you are to be chosen.

I am a professional portrait, sports and commercial photographer located in Brisbane, Australia. I am looking for a professional business card to distribute to professional clients. The card needs to be professional and easy to read. It must have my contact information as listed below.

Industry/Entity Type

Business

Contact Information for Business Card

Dana Wrenfield Photography
www.danawrenfieldphoto.com.au
dana@danawrenfieldphoto.com.au
+61 437 582 906

Font styles to use
Serif
Sans Serif

Colors
ffc214
fece3e
fee18a

Requirements
Must have
• Must have contact information as above,
• Please use a similar colourscheme to the one provided in the logo upload.
Nice to have
• A very simple, design, happy to have some geometric shapes etc. Must look professional

```html
<!DOCTYPE html>
<html lang="en">
<head>
<meta charset="utf-8">
<title>Dana Wrenfield Photography – Business Card</title>
<link rel="stylesheet" href="https://fonts.googleapis.com/css2?family=Questrial&family=Arimo:wght@400&display=swap">
<style>
  :root {
    --page: #ffffff;
    --card-dark: #0c0d0f;
    --card-light: #ffffff;
    --card-edge: #9aa3a8;
    --name-on-dark: #3c4046;
    --name-on-light: #3a3d42;
    --ink: #1f2023;
    --gold: #e0952a;
    --gold-deep: #b8701c;
  }
  * { margin: 0; padding: 0; box-sizing: border-box; }
  html, body {
    width: 1200px; height: 1200px; overflow: hidden;
    background: var(--page);
  }
  .canvas { position: relative; width: 1200px; height: 1200px; }

  .card {
    position: absolute;
    width: 838px; height: 480px;
    border-radius: 40px;
    overflow: hidden;
  }
  .card--front { left: 184px; top: 105px; background: var(--card-dark); }
  .card--back  { left: 177px; top: 614px; background: var(--card-light); border: 1px solid var(--card-edge); }

  .brand-dot {
    position: absolute;
    width: 148px; height: 148px; border-radius: 50%;
    background: radial-gradient(circle at 35% 30%, var(--gold) 0%, var(--gold) 55%, var(--gold-deep) 100%);
  }
  .card--front .brand-dot { left: 136px; top: 165px; }
  .card--back  .brand-dot { left: 147px; top: 134px; }

  .wordmark {
    position: absolute;
    font-family: "Questrial", sans-serif;
    font-weight: 400;
    text-transform: uppercase;
    line-height: 1;
    white-space: nowrap;
  }
  .wordmark__name { display: block; font-size: 50px; letter-spacing: -1.5px; }
  .wordmark__trade { display: block; font-size: 34px; letter-spacing: -1px; margin-top: 4px; }
  .card--front .wordmark { left: 318px; top: 196px; color: var(--name-on-dark); }
  .card--back  .wordmark { left: 323px; top: 168px; color: var(--name-on-light); }

  .contact-list {
    position: absolute; left: 327px; top: 327px;
    list-style: none;
    font-family: "Arimo", sans-serif;
    font-size: 23px; color: var(--ink);
  }
  .contact-list__item { display: flex; align-items: center; height: 36px; }
  .contact-list__icon { width: 22px; height: 22px; margin-right: 18px; flex: none; }
</style>
</head>
<body>
<div class="canvas">

  <section class="card card--front" aria-label="Card front">
    <div class="brand-dot" aria-hidden="true"></div>
    <h1 class="wordmark">
      <span class="wordmark__name">Dana Wrenfield</span>
      <span class="wordmark__trade">Photography</span>
    </h1>
  </section>

  <section class="card card--back" aria-label="Card back">
    <div class="brand-dot" aria-hidden="true"></div>
    <h2 class="wordmark">
      <span class="wordmark__name">Dana Wrenfield</span>
      <span class="wordmark__trade">Photography</span>
    </h2>

    <ul class="contact-list">
      <li class="contact-list__item">
        <svg class="contact-list__icon" viewBox="0 0 24 24" aria-hidden="true">
          <rect x="5" y="1.5" width="14" height="21" rx="3" fill="none" stroke="var(--gold)" stroke-width="2.4"/>
          <circle cx="12" cy="18.5" r="1.4" fill="var(--gold)"/>
        </svg>
        +61 437 582 906
      </li>
      <li class="contact-list__item">
        <svg class="contact-list__icon" viewBox="0 0 24 24" aria-hidden="true">
          <rect x="1" y="5" width="22" height="14" fill="var(--gold)"/>
          <path d="M1 5 L12 13 L23 5 M1 19 L9 11 M23 19 L15 11" fill="none" stroke="#fff" stroke-width="1.4"/>
        </svg>
        dana@danawrenfieldphoto.com.au
      </li>
      <li class="contact-list__item">
        <svg class="contact-list__icon" viewBox="0 0 24 24" aria-hidden="true">
          <circle cx="12" cy="12" r="10.5" fill="var(--gold)"/>
          <g fill="none" stroke="#fff" stroke-width="1.4">
            <ellipse cx="12" cy="12" rx="4.5" ry="10.5"/>
            <line x1="12" y1="1.5" x2="12" y2="22.5"/>
            <line x1="1.5" y1="12" x2="22.5" y2="12"/>
            <path d="M3.5 7 H20.5 M3.5 17 H20.5"/>
          </g>
        </svg>
        www.danawrenfieldphoto.com.au
      </li>
    </ul>
  </section>

</div>
</body>
</html>
```